Real Estate Company / Capital Needs Cards!

need business cards designed using the logos that were just designed by sketchhive.

Reason: per designers request deadline extended 1 day…thank you.

Target Market(s)

Investors and clients looking to purchase real estate or invest in the business.

Industry/Entity Type

Business

Requirements
Must have
• two designs - one for the real estate logo and one for the capital logo, similar but slightly different.
Nice to have
• something to make it pop (perhaps on the back)
Should not have
• much color

```html
<!DOCTYPE html>
<html lang="en">
<head>
<meta charset="utf-8">
<title>Veldan Business Cards</title>
<link rel="stylesheet" href="https://fonts.googleapis.com/css2?family=Mulish:wght@400;600;700&display=swap">
<style>
  :root {
    --backdrop: #e4e1dc;
    --card-black: #0c0c0c;
    --card-white: #ffffff;
    --ink: #1a1a1a;
    --ink-soft: #3a3a3a;
    --brand-grey: #6f6f72;
    --rule: #b5b5b5;
    --on-black: #ffffff;
  }
  * { box-sizing: border-box; margin: 0; padding: 0; }
  html, body {
    width: 1200px; height: 900px; overflow: hidden;
    background: var(--backdrop);
    font-family: "Mulish", sans-serif;
  }
  .canvas { position: relative; width: 1200px; height: 900px; }

  .card {
    position: absolute;
    border-radius: 16px;
    box-shadow: 0 6px 18px rgba(0,0,0,0.25);
    overflow: hidden;
  }
  .card--black { background: var(--card-black); color: var(--on-black); }
  .card--white { background: var(--card-white); color: var(--ink); }

  /* Brand lockup: plain square + name, one font, one weight */
  .brand { display: flex; align-items: center; gap: 14px; font-weight: 600; }
  .brand--stacked { flex-direction: column; gap: 10px; text-align: center; }
  .brand__square { flex: none; background: currentColor; }
  .brand__name { line-height: 1.05; letter-spacing: 0.04em; text-transform: uppercase; }
  .brand__main { display: block; }
  .brand__sub { display: block; letter-spacing: 0.14em; }

  .website {
    position: absolute; left: 0; right: 0; text-align: center;
    font-size: 14px; letter-spacing: 0.02em;
  }
  .website strong { font-weight: 700; }

  /* Capital – front */
  .capital-front { left: 20px; top: 110px; width: 515px; height: 300px; }
  .capital-front .brand { position: absolute; left: 162px; width: 200px; top: 78px; color: var(--on-black); }
  .capital-front .brand__square { width: 90px; height: 90px; border-radius: 9px; }
  .capital-front .brand__main { font-size: 40px; }
  .capital-front .brand__sub { font-size: 14px; }
  .capital-front .website { top: 258px; }

  /* Capital – back */
  .capital-back { left: 100px; top: 412px; width: 500px; height: 293px; }
  .capital-back .brand { position: absolute; left: 20px; width: 130px; top: 18px; color: var(--brand-grey); gap: 8px; }
  .capital-back .brand__square { width: 72px; height: 72px; border-radius: 7px; }
  .capital-back .brand__main { font-size: 28px; }
  .capital-back .brand__sub { font-size: 11px; }
  .capital-back .divider {
    position: absolute; left: 20px; right: 20px; top: 159px; height: 1px; background: var(--rule);
  }
  .person, .details { position: absolute; font-size: 12.5px; line-height: 1.4; color: var(--ink-soft); }
  .person__name { font-size: 15px; font-weight: 700; color: var(--ink); }
  .person__role { font-size: 13px; color: var(--ink-soft); }
  .details__block { margin-top: 12px; }
  .capital-back .person { right: 22px; top: 116px; text-align: right; }
  .capital-back .details { right: 22px; top: 176px; text-align: right; }

  /* Real estate – front */
  .estate-front { left: 600px; top: 195px; width: 520px; height: 300px; }
  .estate-front .brand { position: absolute; left: 140px; top: 120px; color: var(--on-black); gap: 16px; }
  .estate-front .brand__square { width: 60px; height: 60px; border-radius: 7px; }
  .estate-front .brand__main { font-size: 40px; }
  .estate-front .brand__sub { font-size: 15px; }
  .estate-front .website { top: 262px; }

  /* Real estate – back */
  .estate-back { left: 687px; top: 505px; width: 500px; height: 295px; }
  .estate-back .details { left: 0; width: 204px; top: 88px; text-align: right; }
  .estate-back .details__block { margin-top: 10px; }
  .estate-back .vrule { position: absolute; left: 243px; top: 82px; width: 1px; height: 162px; background: var(--ink-soft); }
  .estate-back .brand { position: absolute; left: 272px; top: 132px; color: var(--brand-grey); gap: 12px; }
  .estate-back .brand__square { width: 44px; height: 44px; border-radius: 5px; }
  .estate-back .brand__main { font-size: 28px; }
  .estate-back .brand__sub { font-size: 12px; }
</style>
</head>
<body>
<main class="canvas">

  <section class="card card--black capital-front" aria-label="Veldan Capital card front">
    <div class="brand brand--stacked">
      <span class="brand__square"></span>
      <span class="brand__name"><span class="brand__main">Veldan</span><span class="brand__sub">Capital, LLC</span></span>
    </div>
    <p class="website">www.<strong>veldancapital</strong>.com</p>
  </section>

  <section class="card card--black estate-front" aria-label="Veldan Real Estate card front">
    <div class="brand">
      <span class="brand__square"></span>
      <span class="brand__name"><span class="brand__main">Veldan</span><span class="brand__sub">Real Estate</span></span>
    </div>
    <p class="website">www.<strong>veldanrealestate</strong>.com</p>
  </section>

  <section class="card card--white capital-back" aria-label="Veldan Capital card back">
    <div class="brand brand--stacked">
      <span class="brand__square"></span>
      <span class="brand__name"><span class="brand__main">Veldan</span><span class="brand__sub">Capital, LLC</span></span>
    </div>
    <div class="person">
      <p class="person__name">Mark Holloway</p>
      <p class="person__role">CEO</p>
    </div>
    <div class="divider"></div>
    <div class="details">
      <p>Marlow Park Office,<br>Sandton, South Africa.</p>
      <p class="details__block">Tel: +27 (11) 5550142<br>Mob: +27 700 555 019<br>Email: info@veldancapital.com</p>
    </div>
  </section>

  <section class="card card--white estate-back" aria-label="Veldan Real Estate card back">
    <div class="details">
      <p class="person__name">Mark Holloway</p>
      <p class="person__role">CEO</p>
      <p class="details__block">Marlow Park Office,<br>Sandton, South Africa</p>
      <p class="details__block">T: +27 (11) 5550142<br>M: +27 700 555 019<br>E: info@veldanrealestate.com</p>
    </div>
    <div class="vrule"></div>
    <div class="brand">
      <span class="brand__square"></span>
      <span class="brand__name"><span class="brand__main">Veldan</span><span class="brand__sub">Real Estate</span></span>
    </div>
  </section>

</main>
</body>
</html>
```